Logo needed for business card

Velquist Pty Ltd is in the business of healthcare and ecommerce.

We own and manage pharmacies and online health ecomerce sites.

We provide ecommerce consultants for companies looking for an ecommerce business startegy.

Think of it as the umbrella under which several healthcare brands may sit.

When I think of Velquist, I visulaise slick black/metalic colours, so please stay away from the common blue and green colours that seem to be so popular in this field.

Target Market(s)

CEOs and COOs

Industry/Entity Type

Healthcare

Contact Information for Business Card

Tessa Lindqvist
Director
Velquist Pty Ltd
4/362 Fennick Pde
Brellton, NSW 2148

Requirements
Must have
• Design must have scope to be implemented on the company's website and letterheads etc.

```html
<!DOCTYPE html>
<html lang="en">
<head>
<meta charset="utf-8">
<title>Velquist Pty Ltd — Business Card</title>
<link href="https://fonts.googleapis.com/css2?family=Ubuntu:ital,wght@0,400;0,500;1,400&display=swap" rel="stylesheet">
<style>
  :root {
    --backdrop: #8a8a8a;
    --card: #1d1d1e;
    --card-edge: #262627;
    --ink: #f2f2f2;
    --ink-muted: #d6d6d6;
    --accent: #e3262b;
  }
  html, body {
    margin: 0;
    padding: 0;
    width: 1200px;
    height: 949px;
    overflow: hidden;
    background: var(--backdrop);
  }
  .canvas {
    position: relative;
    width: 1200px;
    height: 949px;
    font-family: "Ubuntu", sans-serif;
  }
  .card {
    position: absolute;
    left: 150px;
    top: 220px;
    width: 900px;
    height: 510px;
    background: var(--card);
    border: 1px solid var(--card-edge);
    box-sizing: border-box;
  }
  .brand {
    position: absolute;
    right: 54px;
    top: 150px;
    text-align: right;
  }
  .brand-name {
    display: flex;
    align-items: center;
    justify-content: flex-end;
    gap: 16px;
    margin: 0;
    font-size: 40px;
    font-weight: 400;
    letter-spacing: 1px;
    color: var(--ink);
  }
  .brand-dot {
    width: 18px;
    height: 18px;
    background: var(--accent);
  }
  .brand-address {
    margin: 8px 0 0;
    font-size: 19px;
    color: var(--ink-muted);
  }
  .person-block {
    position: absolute;
    left: 0;
    top: 316px;
    width: 68px;
    height: 68px;
    background: var(--accent);
  }
  .person {
    position: absolute;
    left: 84px;
    top: 312px;
  }
  .person-name {
    margin: 0;
    font-size: 33px;
    font-weight: 400;
    color: var(--ink);
    line-height: 1.1;
  }
  .person-role {
    margin: 2px 0 0;
    font-size: 31px;
    font-style: italic;
    color: var(--accent);
    line-height: 1.1;
  }
  .contact {
    position: absolute;
    left: 26px;
    top: 392px;
    list-style: none;
    margin: 0;
    padding: 0;
  }
  .contact li {
    display: flex;
    align-items: center;
    gap: 16px;
    color: var(--ink);
    height: 50px;
  }
  .contact .phone { font-size: 29px; }
  .contact .email { font-size: 24px; }
  .contact svg { flex: none; }
</style>
</head>
<body>
<div class="canvas">
  <section class="card" aria-label="Business card">
    <div class="brand">
      <h1 class="brand-name"><span class="brand-dot"></span>Velquist Pty Ltd</h1>
      <p class="brand-address">4/362 Fennick Pde Brellton, NSW 2148</p>
    </div>

    <div class="person-block"></div>
    <div class="person">
      <p class="person-name">Tessa Lindqvist</p>
      <p class="person-role">Director</p>
    </div>

    <ul class="contact">
      <li class="phone">
        <svg width="38" height="38" viewBox="0 0 38 38" aria-hidden="true">
          <circle cx="19" cy="19" r="17" fill="none" stroke="#f2f2f2" stroke-width="2.5"/>
          <path d="M13 10c1.5-1 2.5-.6 3.2.8l1.4 3c.5 1 .2 1.8-.7 2.4l-1 .7c.8 2 2.3 3.6 4.3 4.6l.8-1c.7-.8 1.5-1 2.4-.4l2.8 1.7c1.2.8 1.4 1.8.4 3.1-1.5 2-3.6 2.4-6 1.1-3.9-2.1-6.8-5.3-8.6-9.4-1-2.5-.5-4.8 1-6.6z" fill="#f2f2f2"/>
        </svg>
        <span>000-3198462</span>
      </li>
      <li class="email">
        <svg width="38" height="28" viewBox="0 0 38 28" aria-hidden="true">
          <rect x="2" y="2" width="34" height="24" fill="none" stroke="#f2f2f2" stroke-width="2.5"/>
          <path d="M2 2l17 14L36 2M2 26l12-12M36 26L24 14" fill="none" stroke="#f2f2f2" stroke-width="2.5"/>
        </svg>
        <span>tessa@velquist.com</span>
      </li>
    </ul>
  </section>
</div>
</body>
</html>
```